Beer Bottle Label, Quarrystone Brewing, Beaumont Homestead

Title: Quarrystone Label Design – Beaumont Homestead
Date: November 6, 2015
Contacts: Tom Brennick

PROJECT OVERVIEW
Objective:
• Create look & feel for Quarrystone beer bottle

Description:
• Label design template for beer bottle that carries Quarrystone branding and allows for Handwritten ABV, IBU, SRM, Batch# and Bottle#

Other considerations:
• Quarrystone artwork per beer type

CREATIVE EXECUTION
Branding:
• Brand personality: Scientific, Cultural with purpose
• Fonts: Road Movie, Rockwell Nexta Rust, Lavenderia
• Colors: Orange (C:2 M:72 Y:100 K:0) & black (C:0 M:0 Y:0 K:100)
• Logo: Provided (Quarrystonebottlelabel.ai.jpg) (QuarrystoneLogo-Enhanced.psd)

Beer Description
Beaumont Homestead
6.0% ABV 22.3 IBU Hop Varieties: 2 Grain Varieties: 5

Style: Farmhouse Ale

Description: Named after Henri de Valcourt—better known as the Comte de Beaumont, the Frenchman who enlisted in the American Revolution and went on to become one of Samuel Pritchard's closest allies. The beer is a celebration of the two countries and blends characteristics of a traditional French Saison with the sweetness of an American fall harvest. American corn and wild honey compliment the malted grains and French Saison yeast to give it a slightly sweet flavor. Peach and passion fruit aroma dominate the nose of this complex beer. Sniff then sip… or gulp. The fruit aroma comes from the dry hopping process.

Label Content:
• Include all government-mandated content, below
Brand name Quarrystone Brewing Co.
Class and type designation Farmhouse Ale
(type of malt beverage, eg, Ale, Lager, Stout, etc)
Name and address BREWED AND BOTTLED BY QUARRYSTONE BREWING CO.
487-B Elm Avenue
Farmingdale, NY 11902
Net contents 22 fl oz
• All of the above content must be legible, at least 2mm/6 pt font, contrast well with label background, and be placed on front of label*

Alcohol content ___% ALC/VOL
(alcohol content must be expressed to the nearest 0.1%)
• The above content must be legible, at least 2mm/6 pt font, of the same kind and size of lettering, of equally conspicuous coloring, and can be placed on front, back or side of label*

Government warning GOVERNMENT WARNING:
(1) According to the Surgeon
General, women should not drink alcoholic beverages during
pregnancy because of the risk of birth defects. (2) Consumption of
alcoholic beverages impairs your ability to drive a car or operate
machinery, and may cause health problems.
• The above content must be legible, at least 2mm/6 pt font, 25 characters at most, contrast well with label background, and can be placed on front, back or side of label*

For more information: http://www.brewrules-example.gov/beer/lbl.shtml

*INTERNAL NOTE: Size/style requirements change for 22oz labels.

Design:
• Use Middle of Label for Name, or design

For more information: http://rockmap-example.org/symbols/stdsec/rocksym-sec37.pdf

PRODUCTION
Specs:
• Main label (3.75 in x 4.25 in)
For more information: http://www.capmark-example.com/shop-bottle-type or
https://orders.capmark-example.com/capmark/start_with.cgi?tag=live-uploadyourown-cap-full#_ga=1.000000000.000000000.0000000000

Format:
• Working files: .ai, .psd, .indd
• Print-ready file: hi-res .pdf
• Other font, vector, or image files

website:
www.quarrystonebrewing-example.com

Target Market(s)

Craft Beer Drinkers

Font styles to use
Other font styles liked:
• Road Movie, Lavanderia, Nexta Rust

Requirements
Must have
• Use of Quarrystone Logo(s). Though design should incorporate the style and name of beer, the label layout should be able to be used on additional beer styles.

```html
<!DOCTYPE html>
<html lang="en">
<head>
<meta charset="utf-8">
<title>Quarrystone Brewing – Beaumont Homestead Label</title>
<link rel="stylesheet" href="https://fonts.googleapis.com/css2?family=Lobster&family=Roboto+Slab:wght@700&family=Cabin+Condensed:wght@500;600&family=Dancing+Script:wght@600&display=swap">
<style>
  :root {
    --orange: #ef6a1f;
    --ink: #2b2426;
    --paper: #f6f2ec;
    --stripe-soft: #f1b88f;
    --ground: #dde3e4;
    --white: #ffffff;
  }
  * { box-sizing: border-box; margin: 0; padding: 0; }
  html, body {
    width: 1012px; height: 1200px; overflow: hidden;
    background: var(--ground);
  }
  .sheet { position: relative; width: 1012px; height: 1200px; }

  /* neck label */
  .neck-label {
    position: absolute; left: 642px; top: 150px;
    width: 200px; height: 76px;
  }
  .neck-label .stripe-field { position: absolute; inset: 0; }
  .neck-mark {
    position: absolute; left: 70px; top: 8px;
    width: 60px; height: 60px; border-radius: 50%;
    background: var(--white); border: 3px solid var(--ink);
    display: flex; align-items: center; justify-content: center;
    font-family: "Roboto Slab", serif; font-weight: 700;
    font-size: 8px; color: var(--ink);
  }

  /* main labels */
  .label {
    position: absolute; top: 330px;
    width: 420px; height: 566px;
    background: var(--paper);
  }
  .label--dark { left: 62px; }
  .label--orange { left: 532px; }

  .stripe-field {
    background: linear-gradient(90deg, var(--paper) 0%, var(--stripe-soft) 30%, #e9d8c8 50%, var(--stripe-soft) 70%, var(--paper) 100%);
  }
  .label .stripe-field { position: absolute; left: 24px; right: 24px; top: 0; bottom: 0; }

  .side-copy {
    position: absolute; top: 10px; bottom: 10px; width: 24px;
    font-family: "Cabin Condensed", sans-serif; font-weight: 500;
    font-size: 8.5px; color: var(--ink); white-space: nowrap;
    writing-mode: vertical-rl; overflow: hidden;
    display: flex; align-items: center; justify-content: flex-start;
  }
  .side-copy--left { left: 0; }
  .side-copy--right { right: 0; transform: rotate(180deg); }
  .side-copy .warning-head { color: var(--orange); }

  .stat-band, .volume-band {
    position: absolute; left: 24px; right: 24px; height: 30px;
    display: flex; align-items: center; justify-content: center;
    font-family: "Cabin Condensed", sans-serif; font-weight: 600;
    color: var(--white);
  }
  .stat-band { top: 9px; font-size: 12px; }
  .volume-band { bottom: 9px; font-size: 13px; background: var(--ink); }
  .label--dark .stat-band { background: var(--ink); }
  .label--orange .stat-band { background: var(--orange); color: var(--ink); }

  .brand-seal {
    position: absolute; left: 50%; top: 78px;
    width: 268px; height: 268px; margin-left: -134px;
    border-radius: 50%; background: var(--white);
    border: 6px solid var(--orange);
    display: flex; flex-direction: column; align-items: center; justify-content: center;
    font-family: "Roboto Slab", serif; font-weight: 700; color: var(--ink);
    text-align: center; line-height: 1.1;
  }
  .brand-seal .brand-name { font-size: 34px; }
  .brand-seal .brand-suffix { font-size: 20px; }

  .beer-plate {
    position: absolute; left: 50%; bottom: 40px;
    width: 260px; height: 112px; margin-left: -130px;
    background: var(--ink); border-radius: 130px 130px 0 0;
    display: flex; flex-direction: column; align-items: center; justify-content: flex-end;
    padding-bottom: 12px; text-align: center;
  }
  .beer-name {
    font-family: "Lobster", cursive; font-size: 34px; line-height: 1;
    color: var(--orange);
  }
  .beer-style {
    font-family: "Dancing Script", cursive; font-size: 27px; line-height: 1.1;
    color: var(--white);
  }

  .beer-title {
    position: absolute; left: 0; right: 0; bottom: 48px;
    text-align: center;
  }
  .beer-title .beer-name,
  .beer-title .beer-style {
    color: var(--white);
    -webkit-text-stroke: 1.4px var(--ink);
    paint-order: stroke fill;
  }
  .beer-title .beer-name { font-size: 36px; }
  .beer-title .beer-style { font-size: 32px; }
</style>
</head>
<body>
<main class="sheet">

  <section class="neck-label" aria-label="Neck label">
    <div class="stripe-field" role="img" aria-label="Hand-drawn vertical orange and black stripe pattern"></div>
    <div class="neck-mark">Quarrystone</div>
  </section>

  <section class="label label--dark" aria-label="Main label, dark variant">
    <div class="stripe-field" role="img" aria-label="Hand-drawn vertical orange and black stripe pattern"></div>
    <p class="side-copy side-copy--left">Named after Henri de Valcourt—better known as the Comte de Beaumont, the Frenchman</p>
    <p class="side-copy side-copy--right"><span class="warning-head">GOVERNMENT WARNING:</span>&nbsp;(1) According to the Surgeon General, women should not drink</p>
    <div class="stat-band">22.3 IBU • Hop Varieties: 2 • Grain Varieties: 5</div>
    <div class="brand-seal">
      <span class="brand-name">Quarrystone</span>
      <span class="brand-suffix">Brewing Co.</span>
    </div>
    <div class="beer-plate">
      <span class="beer-name">Beaumont</span>
      <span class="beer-style">Homestead Ale</span>
    </div>
    <div class="volume-band">NET CONTENTS 22 FL.OZ. / ALC 6.0% BY VOLUME</div>
  </section>

  <section class="label label--orange" aria-label="Main label, orange variant">
    <div class="stripe-field" role="img" aria-label="Hand-drawn vertical orange and black stripe pattern"></div>
    <p class="side-copy side-copy--left">Named after Henri de Valcourt—better known as the Comte de Beaumont, the Frenchman</p>
    <p class="side-copy side-copy--right"><span class="warning-head">GOVERNMENT WARNING:</span>&nbsp;(1) According to the Surgeon General, women should not drink</p>
    <div class="stat-band">22.3 IBU • Hop Varieties: 2 • Grain Varieties: 5</div>
    <div class="brand-seal">
      <span class="brand-name">Quarrystone</span>
      <span class="brand-suffix">Brewing Co.</span>
    </div>
    <div class="beer-title">
      <div class="beer-name">Beaumont</div>
      <div class="beer-style">Homestead Ale</div>
    </div>
    <div class="volume-band">NET CONTENTS 22 FL.OZ. / ALC 6.0% BY VOLUME</div>
  </section>

</main>
</body>
</html>
```